Bright Harbor Notes Wordpress Blog

I need to design a WordPress blog page. The name of the Blog is "Bright Harbor Notes". I am hoping for a simple design that is easy for me to post future posts to. I like the color teal for this. The website is brightharbornotes.example where I am going to write a personal blog. I don't have a logo for this, but am hoping for a header that has some swirly, but classy looking text. Easy on the eyes. The website will only have a couple of pages - the home landing page, and an about me page.

Font styles to use
Script

Colors
00a990
86cfc6
cfeae6

Requirements
Must have
• A header for the landing page of the blog. Clean layout of where the blog posts will lie.

```html
<!DOCTYPE html>
<html lang="en">
<head>
<meta charset="utf-8">
<title>Bright Harbor Notes</title>
<link href="https://fonts.googleapis.com/css2?family=Great+Vibes&family=Oswald:wght@400;500;700&family=Open+Sans:wght@400;600;700&display=swap" rel="stylesheet">
<style>
:root{
  --accent:#00a990;
  --accent-mid:#86cfc6;
  --accent-pale:#cfeae6;
  --accent-deep:#007f6c;
  --ink:#2b2b2b;
  --muted:#7a7a7a;
  --line:#e6e6e6;
  --bar:#b9e0da;
  --white:#ffffff;
}
*{box-sizing:border-box;margin:0;padding:0}
html,body{width:1200px;height:2812px;overflow:hidden;background:var(--white)}
body{position:relative;font-family:"Open Sans",Arial,sans-serif;color:var(--ink)}
.abs{position:absolute}
.site-title{left:80px;top:22px;font-family:"Great Vibes",cursive;font-size:46px;line-height:60px;color:var(--accent);font-weight:400}
.nav{right:128px;top:36px;display:flex;gap:28px;align-items:center;font-family:"Oswald",sans-serif;font-size:15px;letter-spacing:1px;font-weight:500}
.search{width:40px;height:40px;border-radius:50%;background:var(--accent);display:flex;align-items:center;justify-content:center}
.share-rail{left:66px;top:140px;width:26px;display:flex;flex-direction:column}
.share-rail span{height:26px;display:block}
.post{left:100px;width:660px;height:600px}
.post .photo{width:660px;height:364px}
.post h2{position:absolute;top:386px;font-family:"Oswald",sans-serif;font-weight:700;font-size:20px;letter-spacing:.5px;text-transform:uppercase}
.post .rule{position:absolute;top:424px;left:0;width:660px;height:2px;background:var(--accent)}
.meta{position:absolute;top:436px;display:flex;gap:34px;align-items:center;font-size:12px;color:var(--muted);text-transform:uppercase}
.meta .item{display:flex;align-items:center;gap:8px}
.avatar{width:24px;height:24px;border-radius:50%;background:#c9a593}
.excerpt{position:absolute;top:472px;font-size:12.5px;line-height:20px;color:#555;width:660px}
.btn{display:inline-block;background:var(--accent);color:var(--white);font-family:"Oswald",sans-serif;font-size:13px;letter-spacing:1px;padding:5px 18px;text-transform:uppercase}
.post .btn{position:absolute;top:530px;left:0}
.post .sep{position:absolute;top:592px;left:0;width:660px;height:1px;background:var(--line)}
.sidebar{left:804px;width:268px}
.ribbon{background:var(--accent);color:var(--white);font-family:"Oswald",sans-serif;font-size:16px;letter-spacing:1px;text-align:center;padding:6px 0;text-transform:uppercase}
.about-text{font-size:12px;line-height:20px;color:#555;padding:16px 4px 0}
.ad{top:700px;height:260px;background:linear-gradient(135deg,var(--accent-mid),var(--accent))}
.social-box{top:972px;height:268px;border:1px solid var(--accent-mid)}
.tabs{display:flex;height:34px}
.tabs div{flex:1;color:var(--white);font-size:14px;display:flex;align-items:center;padding-left:14px}
.social-box .count{font-size:12px;padding:12px;color:#333}
.faces{display:grid;grid-template-columns:repeat(5,40px);gap:10px 10px;padding:0 12px}
.faces span{width:40px;height:40px;background:var(--accent-pale);display:block}
.popular-head{top:1272px}
.pop{width:268px}
.pop .thumb{height:160px}
.pop p{font-size:12px;line-height:18px;color:#444;padding-top:10px}
.footer-line{left:0;top:2528px;width:1200px;height:4px;background:var(--accent)}
.footer{left:0;top:2532px;width:1200px;height:228px;background:var(--accent-pale)}
.footer h3{font-family:"Open Sans",sans-serif;font-size:18px;font-weight:600;margin-bottom:14px}
.col{position:absolute;top:36px;font-size:13px;color:#555;line-height:24px}
.field{width:180px;height:28px;background:var(--white);border:1px solid var(--accent-mid);font-size:12px;padding:4px 8px;color:#999;margin-bottom:10px;line-height:18px}
.contact-row{display:flex;gap:10px;align-items:center}
.circles{display:flex;gap:8px}
.circles span{width:28px;height:28px;border-radius:50%;background:var(--accent);display:block}
.footer-name{font-family:"Great Vibes",cursive;font-size:32px;color:var(--accent);margin-top:22px;line-height:40px}
.copy{left:0;top:2760px;width:1200px;height:52px;background:var(--bar);font-size:12px;color:#3d5f5a;display:flex;align-items:center;justify-content:center}
</style>
</head>
<body>

<header>
  <div class="abs site-title">Bright Harbor Notes</div>
  <nav class="abs nav">
    <span>HOME</span><span>ABOUT MAREN</span><span>CONTACT</span>
    <span class="search"><svg width="18" height="18" viewBox="0 0 18 18"><circle cx="7.5" cy="7.5" r="5" fill="none" stroke="#fff" stroke-width="2"/><line x1="11.5" y1="11.5" x2="16" y2="16" stroke="#fff" stroke-width="2"/></svg></span>
  </nav>
</header>

<div class="abs share-rail" aria-label="Share buttons">
  <span style="background:#007f6c"></span><span style="background:#00a990"></span><span style="background:#3dbba7"></span><span style="background:#86cfc6"></span><span style="background:#b0ddd6"></span>
</div>

<main>
  <article class="abs post" style="top:108px">
    <div class="photo" role="img" aria-label="Photo of colleagues talking in a bright office" style="background:linear-gradient(135deg,#b9b4ac,#e4e0d8 60%,#8a8f96)"></div>
    <h2>Lorem ipsum dolor sit amet, consectetur adipiscing elit</h2>
    <div class="rule"></div>
    <div class="meta"><span class="item"><span class="avatar"></span>By Maren</span><span class="item"><svg width="14" height="12"><rect x="1" y="1" width="12" height="8" rx="1" fill="none" stroke="#00a990" stroke-width="1.5"/><path d="M3 9 L3 12 L6 9" fill="#00a990"/></svg>22 Comments</span><span class="item"><svg width="12" height="12"><rect x="1" y="2" width="10" height="9" fill="none" stroke="#00a990" stroke-width="1.5"/><line x1="1" y1="5" x2="11" y2="5" stroke="#00a990"/></svg>22-06-2017</span></div>
    <p class="excerpt">Small steps add up to real change over time. Here I share notes on habits, focus and calm routines that help me grow a little more each week, with honest lessons from the days that did not go to plan.</p>
    <span class="btn">Read more</span>
    <div class="sep"></div>
  </article>

  <article class="abs post" style="top:708px">
    <div class="photo" role="img" aria-label="Black and white photo of hands joining coloured puzzle pieces" style="background:linear-gradient(135deg,#3a3a3a,#9a9a9a 55%,#d0d0d0)"></div>
    <h2>Lorem ipsum dolor sit amet, consectetur adipiscing elit</h2>
    <div class="rule"></div>
    <div class="meta"><span class="item"><span class="avatar"></span>By Maren</span><span class="item"><svg width="14" height="12"><rect x="1" y="1" width="12" height="8" rx="1" fill="none" stroke="#00a990" stroke-width="1.5"/><path d="M3 9 L3 12 L6 9" fill="#00a990"/></svg>22 Comments</span><span class="item"><svg width="12" height="12"><rect x="1" y="2" width="10" height="9" fill="none" stroke="#00a990" stroke-width="1.5"/><line x1="1" y1="5" x2="11" y2="5" stroke="#00a990"/></svg>22-06-2017</span></div>
    <p class="excerpt">Working with others teaches patience and trust. This post looks at how shared goals bring people together, and how small pieces of effort from each person can fit into one clear picture of progress.</p>
    <span class="btn">Read more</span>
    <div class="sep"></div>
  </article>

  <article class="abs post" style="top:1308px">
    <div class="photo" role="img" aria-label="Illustration of birds flying upward across a pale blue sky with the words vision and growth" style="background:linear-gradient(160deg,#cfe6f5,#9fcbe8 60%,#6fa9d4)"></div>
    <h2>Lorem ipsum dolor sit amet, consectetur adipiscing elit</h2>
    <div class="rule"></div>
    <div class="meta"><span class="item"><span class="avatar"></span>By Maren</span><span class="item"><svg width="14" height="12"><rect x="1" y="1" width="12" height="8" rx="1" fill="none" stroke="#00a990" stroke-width="1.5"/><path d="M3 9 L3 12 L6 9" fill="#00a990"/></svg>22 Comments</span><span class="item"><svg width="12" height="12"><rect x="1" y="2" width="10" height="9" fill="none" stroke="#00a990" stroke-width="1.5"/><line x1="1" y1="5" x2="11" y2="5" stroke="#00a990"/></svg>22-06-2017</span></div>
    <p class="excerpt">A clear vision gives every day a direction. Here are a few simple ways I set long term aims, break them into seasons and weeks, and keep moving forward even when the path ahead looks unclear.</p>
    <span class="btn">Read more</span>
    <div class="sep"></div>
  </article>

  <article class="abs post" style="top:1908px">
    <div class="photo" role="img" aria-label="Photo of cupped hands holding a young green plant in soil" style="background:linear-gradient(135deg,#2e2e2e,#5a5a52 50%,#4f7a2e 75%,#2a2a2a)"></div>
    <h2>Lorem ipsum dolor sit amet, consectetur adipiscing elit</h2>
    <div class="rule"></div>
    <div class="meta"><span class="item"><span class="avatar"></span>By Maren</span><span class="item"><svg width="14" height="12"><rect x="1" y="1" width="12" height="8" rx="1" fill="none" stroke="#00a990" stroke-width="1.5"/><path d="M3 9 L3 12 L6 9" fill="#00a990"/></svg>22 Comments</span><span class="item"><svg width="12" height="12"><rect x="1" y="2" width="10" height="9" fill="none" stroke="#00a990" stroke-width="1.5"/><line x1="1" y1="5" x2="11" y2="5" stroke="#00a990"/></svg>22-06-2017</span></div>
    <p class="excerpt">Growth needs care, time and the right soil. In this note I write about tending new ideas gently, giving them room to root, and celebrating the first small signs that something good is taking hold.</p>
    <span class="btn">Read more</span>
  </article>
</main>

<aside>
  <section class="abs sidebar" style="top:108px">
    <div role="img" aria-label="Portrait photo of the blog author" style="height:260px;background:linear-gradient(160deg,#e8ded6,#c9a890 60%,#8c6a55)"></div>
    <div class="ribbon" style="margin-top:12px">About Maren</div>
    <p class="about-text">Hello and welcome. I write here about growth, good habits and the quiet lessons of everyday life. Pull up a chair and stay a while.</p>
    <span class="btn" style="margin:14px 0 0 80px">Read more</span>
  </section>

  <section class="abs sidebar ad" role="img" aria-label="Advertisement banner for a partner talk series"></section>

  <section class="abs sidebar social-box">
    <div class="tabs"><div style="background:var(--accent-deep)">Circle</div><div style="background:var(--accent-mid)">Stream</div></div>
    <p class="count">8,467 people follow Circle</p>
    <div class="faces" aria-label="Follower avatars"><span></span><span></span><span></span><span></span><span></span><span></span><span></span><span></span><span></span><span></span></div>
  </section>

  <section class="abs sidebar popular-head">
    <div class="ribbon">Popular posts</div>
    <div class="pop" style="margin-top:18px">
      <div class="thumb" role="img" aria-label="Photo of a city skyline reflected in glass" style="background:linear-gradient(135deg,#5d6b78,#b8c2cc)"></div>
      <p>Small daily habits that quietly shape a calmer year ahead</p>
    </div>
    <div class="pop" style="margin-top:84px">
      <div class="thumb" role="img" aria-label="Photo of a hand pointing at a rising bar chart" style="background:linear-gradient(135deg,#3e4a55,#9aa6b0)"></div>
      <p>How I track progress without losing joy along the way</p>
    </div>
    <div class="pop" style="margin-top:84px">
      <div class="thumb" role="img" aria-label="Photo of people meeting around a table by bright windows" style="background:linear-gradient(135deg,#2d4a6a,#a8c0d8)"></div>
      <p>Lessons on teamwork from a season of new beginnings</p>
    </div>
  </section>
</aside>

<div class="abs footer-line"></div>
<footer class="abs footer">
  <div class="col" style="left:128px"><h3>Quick Links</h3><div>Home</div><div>About Maren</div><div>Contact Us</div></div>
  <div class="col" style="left:328px"><h3>Newsletter</h3><div class="field">Your email</div><span class="btn" style="font-size:12px;padding:3px 14px">Subscribe</span></div>
  <div class="col" style="left:600px"><h3>Contact Us</h3>
    <div class="contact-row"><svg width="12" height="16"><path d="M6 1a5 5 0 0 1 5 5c0 4-5 9-5 9S1 10 1 6a5 5 0 0 1 5-5z" fill="#00a990"/></svg>12 Quay Lane, Port Alder</div>
    <div class="contact-row"><svg width="14" height="14"><path d="M3 1l3 3-2 2a8 8 0 0 0 4 4l2-2 3 3-2 2C6 13 1 8 1 3z" fill="#00a990"/></svg>(555) 010-2468</div>
    <div class="contact-row"><svg width="14" height="10"><rect x="0.5" y="0.5" width="13" height="9" fill="none" stroke="#00a990"/><path d="M1 1l6 5 6-5" fill="none" stroke="#00a990"/></svg>hello@brightharbornotes.example</div>
  </div>
  <div class="col" style="left:888px"><h3>Follow Us</h3><div class="circles"><span></span><span></span><span></span><span></span><span></span></div><div class="footer-name">Bright Harbor Notes</div></div>
</footer>
<div class="abs copy">Copyright © 2017, brightharbornotes.example. All Rights Reserved.</div>

</body>
</html>
```